Pinecrest Lockworks Business Card Design

Double Sided Business Card Design for a Locksmith company specializing in Safecracking, safe & vault service.

```html
<!DOCTYPE html>
<html lang="en">
<head>
<meta charset="utf-8">
<title>Pinecrest Lockworks – Business Card</title>
<link rel="stylesheet" href="https://fonts.googleapis.com/css2?family=Roboto:wght@400;500;700;900&display=swap">
<style>
  :root {
    --backdrop: #1b1b1d;
    --card: #222224;
    --green: #1f7a36;
    --green-text: #2c8a3f;
    --white: #f2f2f2;
    --muted: #d9d9d9;
  }
  * { margin: 0; padding: 0; box-sizing: border-box; }
  html, body {
    width: 1200px; height: 800px; overflow: hidden;
    background: var(--backdrop);
    font-family: "Roboto", Arial, sans-serif;
  }
  .canvas { position: relative; width: 1200px; height: 800px; }
  .card {
    position: absolute; left: 362px; width: 472px; height: 262px;
    background: var(--card);
  }
  .card--front { top: 125px; }
  .card--back { top: 421px; }

  .brand { position: absolute; display: flex; align-items: center; }
  .brand__dot { border-radius: 50%; background: var(--green); flex: none; }
  .brand__name {
    color: var(--white); font-weight: 900; text-transform: uppercase;
    line-height: 1.05; letter-spacing: 0.03em;
  }
  .card--front .brand { left: 38px; top: 52px; gap: 8px; }
  .card--front .brand__dot { width: 56px; height: 56px; }
  .card--front .brand__name { font-size: 17px; }
  .card--back .brand { left: 73px; top: 83px; gap: 14px; }
  .card--back .brand__dot { width: 99px; height: 99px; }
  .card--back .brand__name { font-size: 31px; }

  .holder { position: absolute; right: 34px; top: 65px; text-align: right; }
  .holder__name { color: var(--white); font-weight: 700; font-size: 16.5px; letter-spacing: 0.02em; }
  .holder__role { color: var(--green-text); font-size: 11px; letter-spacing: 0.04em; margin-top: 2px; }

  .contacts { position: absolute; left: 41px; top: 155px; list-style: none; }
  .contacts li {
    display: flex; align-items: center; gap: 7px;
    color: var(--white); font-size: 11px; height: 18.7px;
  }
  .contacts svg { width: 11px; height: 11px; flex: none; }

  .address { position: absolute; left: 41px; top: 222px; color: var(--green-text); font-size: 11px; }
  .licence { position: absolute; right: 35px; top: 223px; color: var(--muted); font-size: 9px; }
</style>
</head>
<body>
<div class="canvas">
  <section class="card card--front">
    <div class="brand">
      <span class="brand__dot"></span>
      <span class="brand__name">Pinecrest<br>Lockworks</span>
    </div>
    <div class="holder">
      <div class="holder__name">MARCUS HALE</div>
      <div class="holder__role">MANAGER</div>
    </div>
    <ul class="contacts">
      <li>
        <svg viewBox="0 0 12 12" aria-hidden="true"><circle cx="6" cy="6" r="5.5" fill="none" stroke="#1f7a36"/><path d="M4 3.2l1 .2.4 1.4-.7.6a4 4 0 0 0 1.9 1.9l.6-.7 1.4.4.2 1c-.3.6-1 .9-1.6.7A5.5 5.5 0 0 1 3.3 4.8c-.2-.6.1-1.3.7-1.6z" fill="#1f7a36"/></svg>
        555-014-2270
      </li>
      <li>
        <svg viewBox="0 0 12 12" aria-hidden="true"><circle cx="6" cy="6" r="5.5" fill="none" stroke="#1f7a36"/><rect x="3.2" y="4" width="5.6" height="4" rx=".5" fill="#1f7a36"/><path d="M3.4 4.3L6 6.2l2.6-1.9" fill="none" stroke="#222224" stroke-width=".6"/></svg>
        hello@pinecrestlockworks.com
      </li>
      <li>
        <svg viewBox="0 0 12 12" aria-hidden="true"><circle cx="6" cy="6" r="5.5" fill="none" stroke="#1f7a36"/><circle cx="6" cy="6" r="2.8" fill="none" stroke="#1f7a36" stroke-width=".7"/><path d="M3.2 6h5.6M6 3.2c-1.2 1.6-1.2 4 0 5.6M6 3.2c1.2 1.6 1.2 4 0 5.6" fill="none" stroke="#1f7a36" stroke-width=".6"/></svg>
        pinecrestlockworks.com
      </li>
    </ul>
    <p class="address">1840 Cedar Hollow Rd, Suite 210 Pinecrest , TX , 75001</p>
    <p class="licence">B20481735</p>
  </section>

  <section class="card card--back">
    <div class="brand">
      <span class="brand__dot"></span>
      <span class="brand__name">Pinecrest<br>Lockworks</span>
    </div>
  </section>
</div>
</body>
</html>
```